Visualisation Software brochure

i need a sales brochure for a new visualisation software company called Lumora Spaceworks Pro.
The software has been specifically designed for manufacturers, distributers and retailers in the design / décor / furnishing / building industries. It allows customers can then import unlimited numbers of digital photos of rooms from their own home or take advantage of a library of pre-made photos, and then render different products from your catalogue into that photo to see what the finished look will be.
i have attached:
1) a mock up of the home page of the website
2) example of brochure wording that i have put together (although i am a little unsure about what other words i can add - so any suggestions here would be good)
3) i have attached some examples of other brochures that i like and would like similar designs
I am after a classy brochure used by a large corporate technology company that is given to executives and gives an impression of quality, trustworthiness and innovation.
• the colour blue as per the colours on my website mock up provided in the design brief
• I like simple, smart, clean and uncluttered design
• I like simple, clean and uncluttered design
• I like pictures that fit in with my technology (whether that be home and interior design, mixing virtual world and real world, visualising an idea) rather than basic stock of corporate people
Updates
Target Market(s)
marketing professionals
Industry/Entity Type
Software
Font styles to use
Look and feel
Each slider illustrates characteristics of the customer's brand and the style your logo design should communicate.

```html
<!DOCTYPE html>
<html lang="en">
<head>
<meta charset="utf-8">
<title>Lumora Spaceworks Pro – Brochure</title>
<link rel="stylesheet" href="https://fonts.googleapis.com/css2?family=Oswald:wght@500;600&family=Roboto+Condensed:wght@400&display=swap">
<style>
  :root {
    --page-bg: #e9e9ec;
    --navy: #241f8c;
    --navy-deep: #15125c;
    --sky: #4aa8f0;
    --silver-light: #ffffff;
    --silver-mid: #d9d9dc;
    --silver-dark: #b9b9bd;
    --ink: #1d1a55;
    --white: #ffffff;
  }
  * { margin: 0; padding: 0; box-sizing: border-box; }
  html, body {
    width: 1200px; height: 1061px; overflow: hidden;
    background: var(--page-bg);
  }
  .brochure {
    position: absolute; left: 60px; top: 130px;
    width: 1080px; height: 800px;
    display: grid; grid-template-columns: repeat(4, 1fr);
    box-shadow: 0 12px 30px rgba(0,0,0,.25);
  }
  .panel { position: relative; overflow: hidden; }
  .silver {
    background: linear-gradient(90deg, var(--silver-dark) 0%, var(--silver-light) 45%, var(--silver-mid) 100%);
  }
  .navy {
    background: linear-gradient(160deg, var(--navy) 0%, var(--navy-deep) 100%);
  }
  .band { position: absolute; left: 0; right: 0; }

  /* panel 1 */
  .about { position: absolute; left: 26px; right: 26px; top: 330px; }
  .heading {
    font-family: 'Oswald', sans-serif; font-weight: 600;
    color: var(--sky); font-size: 19px; margin-bottom: 8px;
  }
  .body {
    font-family: 'Roboto Condensed', sans-serif;
    font-size: 13.5px; line-height: 1.32; text-align: justify;
  }
  .about .body { color: var(--ink); }
  .body p + p { margin-top: 14px; }

  /* panel 2 */
  .photo-gallery { top: 210px; height: 350px; background: linear-gradient(135deg, #f4f4f4 0%, #bdbdbd 55%, #6e6e6e 100%); }
  /* panel 3 */
  .photo-living { top: 120px; height: 370px; background: linear-gradient(180deg, #8b8b86 0%, #c9c6b8 45%, #e9e7e1 70%, #6b4b2c 100%); }
  .brand {
    position: absolute; left: 0; right: 0; top: 580px;
    display: flex; align-items: center; justify-content: center; gap: 12px;
    font-family: 'Roboto Condensed', sans-serif; font-size: 17px; color: var(--navy);
    line-height: 1.15;
  }
  .brand-dot { width: 30px; height: 30px; border-radius: 50%; background: var(--navy); flex: none; }

  /* panel 4 */
  .cover { position: absolute; left: 26px; right: 26px; top: 80px; color: var(--white); }
  .title { text-align: right; font-family: 'Oswald', sans-serif; font-weight: 600; line-height: 1.05; }
  .title .line-a { display: block; color: var(--sky); font-size: 34px; }
  .title .line-b { display: block; color: var(--white); font-size: 25px; font-weight: 500; }
  .tagline {
    text-align: right; font-family: 'Oswald', sans-serif; font-weight: 500;
    font-size: 13px; margin: 8px 0 28px;
  }
  .cover .body { color: var(--white); }
</style>
</head>
<body>
<main class="brochure">
  <section class="panel silver">
    <div class="about">
      <h2 class="heading">About Lumora Spaceworks Pro</h2>
      <div class="body">
        <p>Formed in 2013 based on a growing need in the market for a fully functional tool.</p>
        <p>Many other products offer big promises but their short comings impede the success of the retailers. Our goal is to ensure a premium experience for customers and retailers.</p>
        <p>We are very focused to be the obvious leader in this space.</p>
        <p>This is based upon our 12 point methodology to maximise customer satisfaction to 95% percentile and beyond.</p>
      </div>
    </div>
  </section>

  <section class="panel navy">
    <div class="band photo-gallery" role="img" aria-label="Photo of a bright white modern interior with a sculpted ceiling, round pendant lights, a wall screen and a white pedestal table with dark chairs"></div>
  </section>

  <section class="panel silver">
    <div class="band photo-living" role="img" aria-label="Photo of a modern living room with a textured stone feature wall, framed leaf print, white sectional sofa and timber floor"></div>
    <div class="brand">
      <span class="brand-dot"></span>
      <span>Lumora Spaceworks<br>Software Solutions</span>
    </div>
  </section>

  <section class="panel navy">
    <div class="cover">
      <h1 class="title"><span class="line-a">Lumora</span><span class="line-b">Spaceworks Pro</span></h1>
      <p class="tagline">Leading the way in visualisation software</p>
      <h2 class="heading">Innovation redefining retail</h2>
      <div class="body">
        <p>We have a product that is rapidly being seen as the next market leader in interactive visualisation software. Lumora Spaceworks Pro has been developed as an all-inclusive, easy-to-use solution that has been specifically designed for retail businesses within the design, décor, flooring, furnishing, building / renovation and real estate industries.</p>
        <p>Lumora Spaceworks Pro is an innovative and powerful web and/or app-based platform that delivers you the capability to positively transform the overall retail experience of your customers as well as your bottom-line as it helps your customers achieve results by being able to visualise and conceptualise in real time how wonderful their real rooms or new homes could look with your products.</p>
      </div>
    </div>
  </section>
</main>
</body>
</html>
```